Shopify Design for Back Pain Patch

We need a design for the Shopify-based homepage of the new Vortilo Spine Patch.

The Vortilo spine patch absorbs the surface energy produced by your body when you are in pain and redistributes it, reducing your discomfort. It is approximately 5” x 5” in size, with an adhesive backing on one side and a cloth-like exterior that is neutral/light tan in color.

We need a website design that matches our packaging (see attached assets). This includes the blue/orange color scheme and our key messages:

-Natural relief for back pain
-Soothes using your body's natural energy
-Odorless, Gentle, Easy to Use
-Reusable up to 5 days

We are going to be using the Shopify platform for this website, so we'd like the design to be usable with this theme:
http://pliantframe.examplestore.net/pages/theme-features

We will do all of the coding, but please keep this layout in mind for the design.

Target Market(s)

The Vortilo Spine Patch is targeted to people suffering from mild to moderate, chronic back pain, but who desire to continue leading active lives.

Industry/Entity Type

Adhesive

Requirements
Must have
• The design needs to have the same look and feel as the packaging for the back patch. Please feel free to use any of the attached assets in your design (doesn't need to be all).
Should not have
• We do not want to see stock photography other than the assets provided.

```html
<!DOCTYPE html>
<html lang="en">
<head>
<meta charset="utf-8">
<title>Vortilo Spine Patch</title>
<link rel="stylesheet" href="https://fonts.googleapis.com/css2?family=Cabin:ital,wght@0,400;0,600;0,700;1,700&family=PT+Sans:wght@400;700&family=Oswald:wght@600&display=swap">
<style>
:root{
  --orange:#f58220;
  --orange-dark:#e5701a;
  --blue:#1f70b8;
  --blue-dark:#0d5aa6;
  --navy:#1b3f93;
  --sky-top:#9ecdf0;
  --text:#222;
  --grey-bg:#f1f1f1;
  --panel:#e9e9ea;
  --white:#fff;
}
*{box-sizing:border-box;margin:0;padding:0}
html,body{width:1163px;height:1200px;overflow:hidden;background:var(--white);font-family:"PT Sans",sans-serif;color:var(--text)}
.page{position:relative;width:1163px;height:1200px;overflow:hidden}
.header{position:absolute;left:0;top:0;width:1163px;height:120px;background:linear-gradient(#b9dcf5,#eef6fc 70%,#fff)}
.logo{position:absolute;left:186px;top:22px;font-family:"Cabin",sans-serif;font-weight:700;color:var(--orange);font-size:44px;line-height:1}
.logo small{display:block;font-size:24px;margin-top:4px;margin-left:70px}
.social{position:absolute;top:10px;left:873px;display:flex;gap:11px}
.social span{width:27px;height:27px;border-radius:4px;background:var(--blue)}
.nav{position:absolute;top:120px;left:0;width:1163px;height:35px;background:var(--blue);display:flex;align-items:center;padding-left:206px;gap:21px}
.nav a{color:var(--white);text-decoration:none;font-family:"Cabin",sans-serif;font-weight:600;font-size:12.5px}
.hero-band{position:absolute;top:155px;left:0;width:1163px;height:296px;background:var(--orange);border-top:1px solid #fff}
.slider{position:absolute;top:159px;left:174px;width:815px;height:289px;overflow:hidden;background:var(--navy)}
.slider-photo{position:absolute;left:0;top:0;width:420px;height:289px;background:linear-gradient(90deg,#8fa0ad,#d5dfe6 55%,#bcd1e4)}
.slider-panel{position:absolute;left:420px;top:0;width:395px;height:289px;background:linear-gradient(160deg,#5fa8e6,#1f70c8 45%,#23358a)}
.tagline{position:absolute;right:12px;top:32px;width:250px;height:42px;background:var(--orange);border:3px solid #fff;transform:skewX(-12deg);display:flex;align-items:center;justify-content:center}
.tagline span{transform:skewX(12deg);font-family:"Cabin",sans-serif;font-style:italic;font-weight:700;color:#fff;font-size:21px}
.claim{position:absolute;right:17px;background:rgba(40,150,220,.75);color:#fff;font-family:"Oswald",sans-serif;font-size:35px;line-height:48px;padding:0 14px 0 10px;letter-spacing:.5px}
.claim::before{content:"";position:absolute;right:100%;top:24px;width:230px;height:1px;background:rgba(255,255,255,.4)}
.arrow{position:absolute;top:126px}
.dots{position:absolute;left:375px;top:270px;display:flex;gap:4px}
.dots span{width:13px;height:13px;border:1px solid #ccc;background:#555;color:#fff;font-size:9px;text-align:center;line-height:11px}
.dots span.on{background:#fff;color:#333}
.content-bg{position:absolute;top:451px;left:0;width:1163px;height:609px;background:linear-gradient(#e8e8e8,#fff 70px)}
.heading{position:absolute;font-family:"Cabin",sans-serif;font-weight:600;color:var(--orange);font-size:22px}
.intro{position:absolute;left:189px;top:507px;width:556px;font-size:11.2px;line-height:17.1px;text-align:justify}
.step-img{position:absolute;top:642px;width:174px;height:157px;border-radius:8px;background:linear-gradient(90deg,#a9dcf4,#f3b796 30%,#f3b796 70%,#a9dcf4)}
.step-img b{position:absolute;left:6px;top:6px;width:15px;height:15px;border:1.5px solid #fff;border-radius:50%;color:#fff;font-size:10px;text-align:center;line-height:12px;font-weight:400}
.step-cap{position:absolute;top:803px;width:174px;text-align:center;font-size:9px;line-height:11.5px;color:#555}
.step-arrow{position:absolute;top:744px}
.product{position:absolute;top:877px;width:126px;height:104px;border:2px solid var(--orange);background:#fff;padding:6px}
.product div{width:100%;height:100%;background:linear-gradient(#f7f7f7,#e6e6e6)}
.p-name{position:absolute;top:985px;font-size:11px;font-weight:700;letter-spacing:.3px}
.p-price{position:absolute;top:1000px;font-size:11px}
.btn-cart{position:absolute;top:1018px;width:84px;height:20px;border-radius:3px;background:linear-gradient(#3a8fdc,var(--blue-dark));border:1px solid #9cc;color:#fff;font-size:9px;text-align:center;line-height:18px}
.news{position:absolute;left:761px;width:215px;height:59px;background:var(--panel);border:1px solid #ddd}
.date{position:absolute;left:7px;top:7px;width:48px;height:44px;background:var(--orange)}
.date i{display:block;font-style:normal;color:#fff;font-size:11px;font-weight:700;text-align:center;line-height:15px}
.date em{position:absolute;left:3px;bottom:3px;width:42px;height:22px;background:var(--blue);color:#fff;font-style:normal;font-weight:700;font-size:15px;text-align:center;line-height:22px}
.news h4{position:absolute;left:62px;top:7px;width:150px;font-size:10.5px;line-height:12px;color:var(--blue-dark);letter-spacing:.3px}
.news p{position:absolute;left:62px;top:37px;font-size:7.5px;color:var(--orange)}
.contact{position:absolute;left:761px;top:790px;width:214px;height:250px;border:1px solid #ccc;border-radius:3px;background:linear-gradient(90deg,#ddd,#f7f7f7 20%,#f7f7f7 80%,#ddd)}
.ribbon{position:absolute;left:20px;top:-7px}
.field{position:absolute;left:16px;width:181px;height:21px;background:#fff;border:1px solid #ccc;border-radius:3px;font-size:9.5px;color:#555;padding:3px 10px}
.send{position:absolute;left:30px;top:200px;width:151px;height:28px;border-radius:3px;background:linear-gradient(#2f8ae0,var(--blue-dark));color:#fff;font-family:"Cabin",sans-serif;font-size:15px;text-align:center;line-height:28px}
.footer{position:absolute;top:1060px;left:0;width:1163px;height:140px;background:var(--blue-dark)}
.footer-nav{position:absolute;top:10px;left:0;width:100%;text-align:center;font-size:11.5px;color:#fff;letter-spacing:.3px}
.footer-nav span{margin:0 6px}
.copy{position:absolute;top:112px;left:0;width:100%;height:28px;border-top:1px solid #4c8fd0;background:#0a4f96;color:#fff;font-size:9px;text-align:center;line-height:28px}
</style>
</head>
<body>
<div class="page">
  <header class="header">
    <div class="logo">Vortilo<small>Spine Patch</small></div>
    <div class="social"><span aria-label="Social link"></span><span aria-label="Social link"></span><span aria-label="Social link"></span></div>
  </header>
  <nav class="nav">
    <a href="#">HOME</a><a href="#">ABOUT US</a><a href="#">THE VORTILO PATCH</a><a href="#">HOW IT WORKS</a><a href="#">BLOG</a><a href="#">FAQ</a><a href="#">BUY ONLINE NOW</a><a href="#">CONTACT US</a>
  </nav>
  <div class="hero-band"></div>
  <section class="slider">
    <div class="slider-photo" role="img" aria-label="Cyclist in a racing jersey wearing the patch on his lower back"></div>
    <div class="slider-panel"></div>
    <div class="tagline"><span>Reusable up to 5 days</span></div>
    <div class="claim" style="top:102px">Sprains</div>
    <div class="claim" style="top:156px">Sore Muscles</div>
    <div class="claim" style="top:212px">Backache</div>
    <svg class="arrow" style="left:2px" width="30" height="40"><polyline points="26,4 8,20 26,36" fill="none" stroke="#f58220" stroke-width="6"/></svg>
    <svg class="arrow" style="left:784px" width="30" height="40"><polyline points="4,4 22,20 4,36" fill="none" stroke="#f58220" stroke-width="6"/></svg>
    <div class="dots"><span>1</span><span class="on">2</span><span>3</span><span>4</span></div>
  </section>
  <div class="content-bg"></div>

  <h1 class="heading" style="left:188px;top:470px">Welcome to Vortilo Spine Patch</h1>
  <p class="intro">Lorem Ipsum. Proin gravida nibh vel velit auctor aliquet. Aenean sollicitudin, lorem quis bibendum auctor, nisi elit consequat ipsum, nec sagittis sem nibh id elit. Duis sed odio sit amet nibh vulputate cursus a sit amet mauris. Morbi accumsan ipsum velit. Nam nec tellus a odio tincidunt auctor a ornare odio. Sed non mauris vitae erat consequat auctor eu in elit. Class aptent taciti sociosqu ad litora torquent per conubia nostra, per inceptos himenaeos. Mauris in erat justo. Nullam ac urna eu felis dapibus condimentum sit</p>

  <h2 class="heading" style="left:191px;top:612px;font-size:20px">How its works</h2>
  <div class="step-img" style="left:188px" role="img" aria-label="Lower back with a red area of discomfort"><b>1</b></div>
  <div class="step-img" style="left:378px" role="img" aria-label="Patch placed over the area of discomfort"><b>2</b></div>
  <div class="step-img" style="left:569px" role="img" aria-label="Lower back with discomfort reduced, shown in green"><b>3</b></div>
  <svg class="step-arrow" style="left:348px" width="56" height="38"><polygon points="0,13 34,13 34,2 54,19 34,36 34,25 0,25" fill="#f26a3a" opacity=".85"/></svg>
  <svg class="step-arrow" style="left:540px" width="56" height="38"><polygon points="0,13 34,13 34,2 54,19 34,36 34,25 0,25" fill="#f26a3a" opacity=".85"/></svg>
  <p class="step-cap" style="left:188px">Discomfort from lower back pain produces surface energy</p>
  <p class="step-cap" style="left:378px">Place the Vortilo™ Patch on the area of discomfort</p>
  <p class="step-cap" style="left:569px">Lower back discomfort is decreased due to the Vortilo™ Patch</p>

  <h2 class="heading" style="left:188px;top:847px;font-size:20px">Our Prosucts</h2>
  <div class="product" style="left:188px"><div role="img" aria-label="Olive wool sock"></div></div>
  <div class="product" style="left:331px"><div role="img" aria-label="Colourful gel heat packs"></div></div>
  <div class="product" style="left:474px"><div role="img" aria-label="Black winter gloves"></div></div>
  <div class="product" style="left:617px"><div role="img" aria-label="Tan heating pad"></div></div>
  <p class="p-name" style="left:205px">Lorem Ipsum</p><p class="p-price" style="left:205px">Price $100</p><div class="btn-cart" style="left:205px">Add to Chart</div>
  <p class="p-name" style="left:344px">Lorem Ipsum</p><p class="p-price" style="left:344px">Price $100</p><div class="btn-cart" style="left:344px">Add to Chart</div>
  <p class="p-name" style="left:482px">Lorem Ipsum</p><p class="p-price" style="left:482px">Price $100</p><div class="btn-cart" style="left:482px">Add to Chart</div>
  <p class="p-name" style="left:628px">Lorem Ipsum</p><p class="p-price" style="left:628px">Price $100</p><div class="btn-cart" style="left:628px">Add to Chart</div>

  <h2 class="heading" style="left:760px;top:480px;font-size:20px">Latest News</h2>
  <article class="news" style="top:514px"><div class="date"><i>Jan 10</i><em>2013</em></div><h4>Lorem Ipsum. Proin gravi Proin gravida lorem proin</h4><p>10th Jan 2013</p></article>
  <article class="news" style="top:576px"><div class="date"><i>Jan 10</i><em>2013</em></div><h4>Lorem Ipsum. Proin gravi Proin gravida lorem proin</h4><p>10th Jan 2013</p></article>
  <article class="news" style="top:638px"><div class="date"><i>Jan 10</i><em>2013</em></div><h4>Lorem Ipsum. Proin gravi Proin gravida lorem proin</h4><p>10th Jan 2013</p></article>
  <article class="news" style="top:699px"><div class="date"><i>Jan 10</i><em>2013</em></div><h4>Lorem Ipsum. Proin gravi Proin gravida lorem proin</h4><p>10th Jan 2013</p></article>

  <section class="contact">
    <svg class="ribbon" width="176" height="72" viewBox="0 0 176 72">
      <defs><linearGradient id="rb" x1="0" y1="0" x2="0" y2="1"><stop offset="0" stop-color="#2f8ae0"/><stop offset="1" stop-color="#0d5aa6"/></linearGradient></defs>
      <path d="M4 4 H172 V52 Q88 76 4 52 Z" fill="url(#rb)"/>
      <text x="88" y="34" text-anchor="middle" font-family="Cabin, sans-serif" font-weight="700" font-style="italic" font-size="17" fill="#fff">QUICK CONTACT</text>
    </svg>
    <div class="field" style="top:71px">Name</div>
    <div class="field" style="top:99px">Email</div>
    <div class="field" style="top:127px;height:64px">Message</div>
    <div class="send">Send</div>
  </section>

  <footer class="footer">
    <p class="footer-nav">Home <span>|</span> About Us <span>|</span> The Vortilo Patch <span>|</span> How It Works <span>|</span> Blog <span>|</span> FAQ <span>|</span> Buy Online Now <span>|</span> Contact Us</p>
    <p class="copy">Copyright 2013 &nbsp;Vortilo Spine Patch. All rights reserved.</p>
  </footer>
</div>
</body>
</html>
```